Business Card Design

The business is a mobile physiotherapy, personal training and massage business located on the Sunreef Coast. I would like a design that works well with my logo that I had recently created by a graphic design company.

I have a mock business card made from the prinwell website. This may help with the design.

Target Market(s)

Any age although specifically for 30+

Industry/Entity Type

Graphic Design

Contact Information for Business Card

Summit Motion Physio
Mobile Physiotherapy, Personal Training & Massage Service
Location: Sunreef Coast
Marcus Tellwin
Dr. of Physiotherapy & B. Ex. Science
e: summitmotionphysio@mailbox.example
w: www.summitmotionphysio.example
m: 0455 726 309

```html
<!DOCTYPE html>
<html lang="en">
<head>
<meta charset="utf-8">
<title>Summit Motion Physio – Business Card</title>
<link rel="stylesheet" href="https://fonts.googleapis.com/css2?family=Roboto:wght@400;700;900&display=swap">
<style>
  :root {
    --page: #e6e6e6;
    --paper: #ffffff;
    --red: #d12027;
    --red-deep: #a81c22;
    --ink: #1b1b1b;
    --white: #ffffff;
  }
  * { margin: 0; padding: 0; box-sizing: border-box; }
  html, body {
    width: 1200px; height: 900px; overflow: hidden;
    background: var(--page);
    font-family: "Roboto", Arial, sans-serif;
  }
  .card {
    position: absolute;
    left: 330px;
    width: 540px; height: 310px;
    background: var(--paper);
    box-shadow: 0 8px 24px rgba(0,0,0,.18);
    overflow: hidden;
  }
  .card--front { top: 110px; }
  .card--back  { top: 480px; }

  .brand {
    position: absolute;
    display: flex; align-items: center; gap: 12px;
    color: var(--ink);
    font-weight: 900;
    white-space: nowrap;
  }
  .brand__dot {
    border-radius: 50%;
    background: var(--red);
    flex: none;
  }
  .card--front .brand { left: 60px; top: 112px; font-size: 38px; }
  .card--front .brand__dot { width: 40px; height: 40px; }
  .tagline {
    position: absolute; left: 60px; top: 172px;
    font-size: 11px; font-weight: 700; letter-spacing: .4px;
    color: var(--ink);
  }

  .card--back .brand { left: 30px; top: 40px; font-size: 27px; }
  .card--back .brand__dot { width: 30px; height: 30px; }
  .wave { position: absolute; inset: 0; width: 540px; height: 310px; }

  .holder {
    position: absolute; left: 30px; top: 238px;
    color: var(--white);
  }
  .holder__name { font-size: 22px; font-weight: 700; letter-spacing: .5px; }
  .holder__title { font-size: 14px; margin-top: 3px; }

  .contacts {
    position: absolute; left: 272px; top: 146px;
    color: var(--white); font-size: 12px; line-height: 19px;
    list-style: none; white-space: nowrap;
  }
  .contacts b { font-weight: 700; }
</style>
</head>
<body>

<section class="card card--front">
  <div class="brand"><span class="brand__dot"></span>Summit Motion Physio</div>
  <p class="tagline">MOBILE PHYSIOTHERAPY, MASSAGE AND PERSONAL TRAINING SERVICE</p>
</section>

<section class="card card--back">
  <svg class="wave" viewBox="0 0 540 310" aria-hidden="true">
    <defs>
      <linearGradient id="redFill" x1="0" y1="0" x2="0" y2="1">
        <stop offset="0" stop-color="#d8232a"/>
        <stop offset="1" stop-color="#a81c22"/>
      </linearGradient>
    </defs>
    <path d="M0 150 Q270 100 540 58 L540 78 Q270 120 0 170 Z" fill="#111"/>
    <path d="M0 176 Q270 126 540 84 L540 310 L0 310 Z" fill="url(#redFill)"/>
  </svg>

  <div class="brand"><span class="brand__dot"></span>Summit Motion Physio</div>

  <ul class="contacts">
    <li><b>Mobile:</b> 0455 726 309</li>
    <li><b>Email:</b> summitmotionphysio@mailbox.example</li>
    <li><b>Website:</b> www.summitmotionphysio.example</li>
    <li><b>Location:</b> Sunreef Coast</li>
  </ul>

  <div class="holder">
    <p class="holder__name">MARCUS TELLWIN</p>
    <p class="holder__title">Dr. of Physiotherapy &amp; B. Ex. Science</p>
  </div>
</section>

</body>
</html>
```